Brochure Design Project

I am looking for a trifold brochure.
I would like it to be square (5.5 x 5.5)
The back needs to be reserved for a map and logo information.

we are a financial planning firm. we have been in operation for 15 years.
our clients are ecstatic and continue to refer others to us.

Brochure COPY:
Building Wealth, Building Futures
We start with your goals. Then we build a comprehensive strategy to manage your investments, grow your wealth, minimize your tax burden and protect your family. Most importantly, we keep you informed about market change, opportunities and concerns before they impact you, so you can make confident decisions about your future, every step of the way.

Understanding and Expertise (bios)
Steadfast Money Partners is led by Marla Tofvenson and Rosalind Pike, experienced business partners who take the time to listen to you, understand your needs and present you with all your options.
Our focus in on your future, and building a confident and financially secure path for you and your family for the years ahead.

Marla Tofvenson, BSc, MBA, CPA, CA, CFP, FMA, CPCA
Certified Financial Planner

With years of experience in tax, investment, estate and retirement issues - and an extensive business background - Marla provided her clients with important financial insights and clear direction in a friendly and open manner.

Rosalind Pike, BSEd, FMA, CPCA, CFP, FCSI, CIM

After a successful tennis career Rosalind joined Marla in the financial industry. Rosalind quickly discovered how much she enjoys working with people and helping them to achieve their goals. Leveraging the discipline and work ethic developed during her tennis career, Rosalind has been instrumental in creating the successful process used by Steadfast Money Partners.

People Trust Us to Help Them
The important things in life are often neglected due to the demands of day to day, including financial planning and wealth management. But it doesn't have to be that way when you have a trustworthy team looking out for you.
At Steadfast Money Partners we have the knowledge, experience and resources to help you move forward and realize your financial goals.

(side note) on the back of the brochure it should have the SMP logo, the office address, 382 Quillbrook Rd. E. Mississauga, ON L5R 7K9, and our website address.

Reason: Am juggling a number of different projects so need to extend the deadline on this one. Will provide copy for the project by end of day today.

Target Market(s)

We would like the brochure to appeal to the high net worth client who is currently working with an advisor but is not getting the attention from them.

Industry/Entity Type

Financial

Requirements
Must have
• SMP Logo on the front. The logo is blue with black font and has a tagline with it that says "Choose your path, change your future."
you can see the logo at www.plotyourmorrow.ca

One page must be about the two advisors, Marla Tofvenson and Rosalind Pike.
(leave an open area for bios and we will fill it in)

We want it to talk about building wealth and passing it on to the next generation.
Should not have
• Financial lingo.

```html
<!DOCTYPE html>
<html lang="en">
<head>
<meta charset="utf-8">
<title>Steadfast Money Partners – Brochure Panel</title>
<link rel="stylesheet" href="https://fonts.googleapis.com/css2?family=BenchNine:wght@400&family=Hind:wght@400&display=swap">
<style>
  :root {
    --page-grey: #dcdcdc;
    --panel-blue: #0b87d1;
    --body-ink: #15212e;
    --heading-white: #ffffff;
    --photo-sky-top: #c6dbee;
    --photo-sky-low: #e4ecf3;
    --photo-base: #6f8fae;
  }
  * { margin: 0; padding: 0; box-sizing: border-box; }
  html, body {
    width: 1200px;
    height: 1198px;
    overflow: hidden;
    background: var(--page-grey);
  }
  .brochure-panel {
    position: absolute;
    left: 50px;
    top: 50px;
    width: 1101px;
    height: 1099px;
    background: var(--panel-blue);
  }
  .panel-copy {
    position: absolute;
    left: 52px;
    width: 995px;
    font-family: "Hind", "Segoe UI", sans-serif;
    font-size: 29px;
    letter-spacing: 0.9px;
    line-height: 40px;
    color: var(--body-ink);
    text-align: justify;
  }
  .bio-copy { top: 72px; }
  .trust-section { top: 355px; }
  .trust-heading {
    font-family: "BenchNine", "Arial Narrow", sans-serif;
    font-weight: 400;
    font-size: 50px;
    letter-spacing: 0;
    line-height: 60px;
    color: var(--heading-white);
    text-align: left;
  }
  .trust-section p { margin: 0; }
  .golf-photo {
    position: absolute;
    left: 283px;
    top: 756px;
    width: 552px;
    height: 343px;
    background: linear-gradient(180deg, var(--photo-sky-top) 0%, var(--photo-sky-low) 55%, var(--photo-base) 100%);
  }
</style>
</head>
<body>
  <main class="brochure-panel">
    <p class="panel-copy bio-copy">After a successful tennis career Rosalind joined Marla in the financial industry. Rosalind quickly discovered how much she enjoys working with people and helping them to achieve their goals. Leveraging the discipline and work ethic developed during her tennis career, Rosalind has been instrumental in creating the successful process used by Steadfast Money Partners.</p>

    <section class="panel-copy trust-section">
      <h2 class="trust-heading">People Trust Us to Help Them</h2>
      <p>The important things in life are often neglected due to the demands of day to day, including financial planning and wealth management. But it doesn't have to be that way when you have a trustworthy team looking out for you.</p>
      <p>At Steadfast Money Partners we have the knowledge, experience and resources to help you move forward and realize your financial goals.</p>
    </section>

    <div class="golf-photo" role="img" aria-label="Photo of a golfer mid-swing under a bright cloudy sky"></div>
  </main>
</body>
</html>
```